a book cover featuring an american west vibe and the image of a coyote.
The author is Walter Brantley
It needs to say "Meridian Dispatch Bestselling Author" above his name.
It needs to have "Introduction by Dean Brantley" in smaller type (perhaps as a round "sticker" to go on the cover as an added element.
The book is called
Ashes of Red Mesa
there will be a subtitle
Where the prairie kept its own quiet laws
I'm looking for a gorgeous and elegant type. I've attached a couple of samples.
I want to thank everyone who contributed a design. It was very difficult to choose. In fact, the family of the author made the final decision and I think they chose well too. I was overwhelmed by the quality of your work.

```html
<!DOCTYPE html>
<html lang="en">
<head>
<meta charset="utf-8">
<title>Ashes of Red Mesa — Walter Brantley</title>
<link rel="stylesheet" href="https://fonts.googleapis.com/css2?family=Cinzel:wght@400;500&family=Oswald:wght@500&family=Arimo&display=swap">
<style>
  :root {
    --sky-top: #8a5a22;
    --sky-mid: #d49a3a;
    --sky-glow: #f7e39a;
    --haze: #e9c878;
    --ridge: #c58f5c;
    --field: #a3773f;
    --field-dark: #5e4222;
    --title-top: #141008;
    --title-bottom: #9e1a10;
    --ink: #1c1710;
    --paper: #ffffff;
  }
  * { margin: 0; padding: 0; box-sizing: border-box; }
  html, body { width: 750px; height: 1200px; overflow: hidden; background: #ffffff; }
  .cover {
    position: relative;
    width: 750px;
    height: 1200px;
    overflow: hidden;
  }
  .cover-art {
    position: absolute;
    inset: 0;
    background:
      radial-gradient(ellipse 60px 30px at 406px 708px, #fffbe6 0%, rgba(255,250,220,0.8) 40%, rgba(255,240,180,0) 100%),
      radial-gradient(ellipse 520px 340px at 400px 700px, rgba(250,232,160,0.95) 0%, rgba(240,200,110,0.5) 45%, rgba(210,150,60,0) 100%),
      linear-gradient(180deg,
        var(--sky-top) 0%,
        #b27a30 14%,
        var(--sky-mid) 36%,
        var(--haze) 55%,
        var(--sky-glow) 62%,
        #e7c27e 70%,
        var(--ridge) 78%,
        var(--field) 85%,
        #8a6231 93%,
        var(--field-dark) 100%);
  }
  .intro-credit {
    position: absolute;
    top: 30px;
    left: 180px;
    font-family: "Cinzel", serif;
    font-size: 17px;
    letter-spacing: 0.5px;
    color: var(--paper);
  }
  .title {
    position: absolute;
    top: 0;
    left: 0;
    width: 750px;
    font-family: "Oswald", sans-serif;
    font-weight: 500;
    text-transform: uppercase;
    text-align: center;
  }
  .title-line {
    position: absolute;
    left: 0;
    width: 100%;
    line-height: 1;
    background: linear-gradient(180deg, var(--title-top) 20%, var(--title-bottom) 95%);
    -webkit-background-clip: text;
    background-clip: text;
    color: transparent;
  }
  .title-line--one { top: 92px; font-size: 134px; }
  .title-line--two { top: 232px; font-size: 166px; }
  .title-line--three { top: 394px; font-size: 160px; }
  .subtitle {
    position: absolute;
    top: 680px;
    left: 172px;
    font-family: "Arimo", sans-serif;
    font-size: 20px;
    line-height: 1.3;
    text-transform: uppercase;
    color: var(--ink);
  }
  .subtitle span { display: block; }
  .subtitle span + span { padding-left: 16px; }
  .author-label {
    position: absolute;
    top: 1052px;
    left: 0;
    width: 100%;
    text-align: center;
    font-family: "Cinzel", serif;
    font-size: 20px;
    color: var(--paper);
  }
  .author-name {
    position: absolute;
    top: 1104px;
    left: 0;
    width: 100%;
    text-align: center;
    font-family: "Cinzel", serif;
    font-size: 66px;
    line-height: 1;
    color: var(--paper);
  }
</style>
</head>
<body>
  <main class="cover">
    <div class="cover-art" role="img" aria-label="Photograph of a coyote standing in dry prairie grass beneath a hazy golden desert sky, with rocky hills and a low sun on the horizon"></div>

    <p class="intro-credit">Introduction by Dean Brantley</p>

    <h1 class="title">
      <span class="title-line title-line--one">Ashes</span>
      <span class="title-line title-line--two">Of Red</span>
      <span class="title-line title-line--three">Mesa</span>
    </h1>

    <p class="subtitle">
      <span>Where the prairie kept its own</span>
      <span>quiet laws</span>
    </p>

    <p class="author-label">Meridian Dispatch Bestselling Author</p>
    <p class="author-name">Walter Brantley</p>
  </main>
</body>
</html>
```